" Trata-se de uma clínica em início de funcionamento. Somos dois responsáveis técnicos (Psicólogos) e temos outros seis profissionais que estarão trabalhando conosco (também psicólogos). Temos uma médica Psiquiatra que fará parte da equipe. Ofereceremos atendimento nas abordagens: terapia cognitivo comportamental, humanista, psicanálise e Gestalt, entretanto, o foco será na Terapia Cognitivo-Comportamental (TCC). De forma breve, a base da TCC é: Nossos pensamentos, emoções e comportamentos estão interligados e influenciam um ao outro e são o foco principal do tratamento. Fazemos atendimentos individuais e em grupo. Além dos atendimentos de psicologia, a nossa proposta é oferecer outros serviços como palestras, cursos, treinamentos. Disponibilizamos de auditório para uso da clínica. No meu caso, tenho forte vínculo acadêmico. Sou pesquisadora do Núcleo de Estudos Clínicos da UNEVAR e faço mestrado em Saúde Mental na mesma instituição. Também pós-graduanda em TCC. Então o ensino será algo que terá um investimento forte, juntamente com os atendimentos clínicos. "

```html
<!DOCTYPE html>
<html lang="pt-BR">
<head>
<meta charset="UTF-8">
<title>Lumina Psicologia — Cartão de visita</title>
<link href="https://fonts.googleapis.com/css2?family=Montserrat:wght@300;400;600&display=swap" rel="stylesheet">
<style>
  :root {
    --page: #eeeeec;
    --card-light: #ffffff;
    --card-dark: #0f2c48;
    --teal: #5cb8ad;
    --teal-soft: #8fd3c8;
    --navy-text: #163454;
    --grey-text: #5a6470;
    --divider: #c9ced4;
  }
  * { margin: 0; padding: 0; box-sizing: border-box; }
  html, body { width: 1200px; height: 1200px; overflow: hidden; }
  body {
    background: var(--page);
    font-family: "Montserrat", Arial, sans-serif;
    position: relative;
  }
  .card {
    position: absolute;
    left: 150px;
    width: 900px;
    height: 515px;
    border-radius: 34px;
  }
  .card--front {
    top: 50px;
    background: var(--card-light);
    border-bottom: 10px solid var(--teal);
    box-shadow: 0 2px 6px rgba(0,0,0,0.08);
  }
  .card--back {
    top: 635px;
    background: var(--card-dark);
    box-shadow: 0 2px 6px rgba(0,0,0,0.12);
  }

  .brand {
    position: absolute;
    display: flex;
    align-items: center;
    gap: 26px;
  }
  .brand__dot {
    border-radius: 50%;
    background: linear-gradient(135deg, var(--teal-soft), var(--teal));
    flex: none;
  }
  .brand__name {
    font-weight: 300;
    line-height: 1;
    text-transform: uppercase;
  }
  .brand__name span { display: block; }

  .card--front .brand { left: 70px; top: 185px; }
  .card--front .brand__dot { width: 70px; height: 70px; }
  .card--front .brand__name { color: var(--navy-text); font-size: 56px; letter-spacing: 2px; }
  .card--front .brand__name .brand__line2 { font-size: 19px; letter-spacing: 12px; margin-top: 10px; }

  .card--back .brand { left: 200px; top: 170px; }
  .card--back .brand__dot { width: 110px; height: 110px; }
  .card--back .brand__name { color: #ffffff; font-size: 96px; letter-spacing: 3px; }
  .card--back .brand__name .brand__line2 { font-size: 30px; letter-spacing: 22px; margin-top: 14px; }

  .divider {
    position: absolute;
    left: 460px;
    top: 120px;
    width: 1px;
    height: 280px;
    background: var(--divider);
  }
  .person { position: absolute; left: 500px; top: 125px; }
  .person__name { font-size: 30px; font-weight: 600; color: var(--navy-text); }
  .person__role { font-size: 17px; color: var(--grey-text); margin-top: 4px; }

  .contacts { position: absolute; left: 500px; top: 225px; list-style: none; }
  .contacts li {
    display: flex;
    align-items: flex-start;
    gap: 14px;
    font-size: 19px;
    color: var(--grey-text);
    margin-bottom: 14px;
    line-height: 1.25;
  }
  .contacts svg { width: 26px; height: 26px; flex: none; }
</style>
</head>
<body>

  <section class="card card--front" aria-label="Frente do cartão">
    <div class="brand">
      <div class="brand__dot"></div>
      <div class="brand__name"><span>Lumina</span><span class="brand__line2">Psicologia</span></div>
    </div>

    <div class="divider"></div>

    <div class="person">
      <p class="person__name">Nome e Sobrenome</p>
      <p class="person__role">Cargo | Função</p>
    </div>

    <ul class="contacts">
      <li>
        <svg viewBox="0 0 26 26"><circle cx="13" cy="13" r="13" fill="#5cb8ad"/><path d="M9 7.5c.6-.4 1.3-.3 1.6.3l1 2c.2.5 0 1-.4 1.3l-.7.5c.6 1.4 1.6 2.5 3 3.1l.5-.7c.3-.4.9-.6 1.3-.3l2 1c.6.3.7 1 .3 1.6-.9 1.3-2.3 1.6-3.6.9-2.5-1.3-4.4-3.2-5.6-5.7-.6-1.3-.3-2.7 1-3.7z" fill="#fff"/></svg>
        <span>(00) 0000-0000</span>
      </li>
      <li>
        <svg viewBox="0 0 26 26"><circle cx="13" cy="13" r="13" fill="#5cb8ad"/><rect x="7" y="8.5" width="12" height="9" rx="1" fill="none" stroke="#fff" stroke-width="1.6"/><path d="M7.5 9.5l5.5 4.5 5.5-4.5" fill="none" stroke="#fff" stroke-width="1.6"/></svg>
        <span>contato@exemplo.com</span>
      </li>
      <li>
        <svg viewBox="0 0 26 26"><circle cx="13" cy="13" r="13" fill="#5cb8ad"/><circle cx="13" cy="13" r="6" fill="none" stroke="#fff" stroke-width="1.5"/><ellipse cx="13" cy="13" rx="2.6" ry="6" fill="none" stroke="#fff" stroke-width="1.3"/><path d="M7 13h12" stroke="#fff" stroke-width="1.3"/></svg>
        <span>www.exemplo.com</span>
      </li>
      <li>
        <svg viewBox="0 0 26 26"><circle cx="13" cy="13" r="13" fill="#5cb8ad"/><path d="M13 6.5a4.5 4.5 0 0 1 4.5 4.5c0 3.3-4.5 8.5-4.5 8.5S8.5 14.3 8.5 11A4.5 4.5 0 0 1 13 6.5z" fill="#fff"/><circle cx="13" cy="11" r="1.7" fill="#5cb8ad"/></svg>
        <span>rua exemplo, sl 000<br>cidade-UF, CEP: 00000-000</span>
      </li>
    </ul>
  </section>

  <section class="card card--back" aria-label="Verso do cartão">
    <div class="brand">
      <div class="brand__dot"></div>
      <div class="brand__name"><span>Lumina</span><span class="brand__line2">Psicologia</span></div>
    </div>
  </section>

</body>
</html>
```